New Brochure Design for multiple brochures

We are looking for a designer to create a new template for our vireLUX family of modular and mobile biopharmaceutical facilities. We will be looking to put together a set of new brochures based on this design, likely using the original designer to complete the final layouts. The attached brochure is true to our current aesthetic and contains our basic corporate color scheme. However, we are open to changes to the colors and the overall look so long as they work with our logo. (FYI: Our president favors clean designs with abundant white space.) Overall, we are hoping to achieve a design that projects the high-tech nature of our company and equipment. This equipment is designed for and sold to biotech and pharmaceutical companies and the brochures should cater to that audience in their visual style.

Target Market(s)

Pharmaceutical Industry

Industry/Entity Type

Biotechnology

Font styles to use
Sans Serif

Requirements
Must have
• A layout design that provides a fresh look on the current brochures attached to this brief. The desired layout would have clean lines with a technology company feel. White space and a design that has a layout with sufficient spacing is important.
Nice to have
• Really like the idea of having a theme that emphasizes a product life cycle and conveys life science technology (gene therapy, cancer drug development) focus.
Should not have
• Cluttered objects and text. Must use the current logo format.

```html
<!DOCTYPE html>
<html lang="en">
<head>
<meta charset="utf-8">
<title>Virelux Brochure Spread</title>
<link href="https://fonts.googleapis.com/css2?family=Montserrat:wght@400;600;800&display=swap" rel="stylesheet">
<style>
  :root {
    --backdrop: #a9b1cf;
    --paper: #ffffff;
    --page-grey: #e3e3e3;
    --navy: #1f2f7a;
    --slate-blue: #7d90b6;
    --mid-grey: #c4c4c4;
    --text-grey: #5a5a5a;
    --photo-light: #ececec;
    --photo-dark: #8d8d8d;
  }
  * { box-sizing: border-box; margin: 0; padding: 0; }
  html, body {
    width: 1200px; height: 674px; overflow: hidden;
    background: var(--backdrop);
    font-family: "Montserrat", Arial, sans-serif;
  }
  .spread {
    position: absolute; left: 40px; top: 137px;
    width: 1120px; height: 400px;
    display: flex;
    box-shadow: 0 10px 30px rgba(40, 50, 90, 0.25);
  }
  .page { position: relative; width: 560px; height: 400px; overflow: hidden; }
  .page--back { background: var(--paper); }
  .page--cover { background: var(--page-grey); }

  .brand { display: flex; align-items: center; gap: 7px; color: var(--navy); font-weight: 600; }
  .brand__mark { background: var(--navy); flex: none; }
  .brand__name { line-height: 1; letter-spacing: 0.04em; white-space: nowrap; }

  .back-contact { position: absolute; left: 60px; top: 120px; }
  .back-contact .brand { margin-bottom: 10px; }
  .back-contact .brand__mark { width: 12px; height: 12px; }
  .back-contact .brand__name { font-size: 12px; }
  .contact-lines { font-size: 9px; line-height: 1.5; color: var(--text-grey); font-style: normal; }
  .contact-lines .web { color: var(--navy); font-weight: 600; }

  .cover-art { position: absolute; inset: 0; }

  .cover-copy { position: absolute; left: 405px; top: 105px; width: 140px; }
  .cover-headline {
    font-size: 24px; font-weight: 800; line-height: 1.05; color: var(--navy);
    margin-bottom: 10px;
  }
  .cover-intro { font-size: 10px; line-height: 1.4; color: var(--text-grey); }

  .cover-brand { position: absolute; right: 30px; bottom: 34px; }
  .cover-brand .brand__mark { width: 16px; height: 16px; }
  .cover-brand .brand__name { font-size: 15px; }
</style>
</head>
<body>
  <main class="spread">
    <section class="page page--back">
      <div class="back-contact">
        <div class="brand">
          <span class="brand__mark"></span>
          <span class="brand__name">VIRELUX STELLANE</span>
        </div>
        <address class="contact-lines">
          Nine Harbor Lane<br>
          Clearwater Bay, FL 33001 USA<br>
          International +1 555-014-2290<br>
          info@stellane.com<br>
          <span class="web">www.stellane.com</span>
        </address>
      </div>
    </section>

    <section class="page page--cover">
      <svg class="cover-art" width="560" height="400" viewBox="0 0 560 400">
        <defs>
          <radialGradient id="photoTone" cx="45%" cy="40%" r="65%">
            <stop offset="0%" stop-color="var(--photo-light)"/>
            <stop offset="100%" stop-color="var(--photo-dark)"/>
          </radialGradient>
        </defs>
        <path class="accent-drop" d="M110 0 C50 80 15 160 20 235 C30 330 120 390 200 380 L200 0 Z" fill="var(--slate-blue)"/>
        <circle class="grey-drop" cx="235" cy="235" r="160" fill="var(--mid-grey)" opacity="0.9"/>
        <circle cx="205" cy="185" r="125" fill="url(#photoTone)" role="img"
                aria-label="Black and white photo of a scientist in a lab coat working at a laboratory bench"/>
      </svg>

      <div class="cover-copy">
        <h1 class="cover-headline">Brochure Template Headline</h1>
        <p class="cover-intro">Verunti usamet ipicia ditam voluptia derit, ut inverum fugitatus destior erepuda que</p>
      </div>

      <div class="brand cover-brand">
        <span class="brand__mark"></span>
        <span class="brand__name">VIRELUX STELLANE</span>
      </div>
    </section>
  </main>
</body>
</html>
```